Kalvendor Whitmane & Associates

We would like a simple, professional business card using a similar font to our logo.

Industry/Entity Type

Law Firm

Contact Information for Business Card

Martin Kalvendor, Esq. 48 Fennimore Lane, 2nd Floor Ashmere, ME 04173 Office: 555.216.4093 Cell: 555.370.8154 Email: marty@kwlawfirm.example kalvendorwhitmanelaw.example

Font styles to use
Other font styles liked:
• We would like to use the fonts used in the logo or similar

Colors
0054AA
0677BA
7BADD7
CADEEF
E8F1F8

Requirements
Must have
• We would like the fonts to match the logo
Nice to have
• not too much design- very simple and professional business card. I added a picture of a business card that I tried to start but I am not a designer! Hopefully it will help with the address and phone numbers and kind of what we are looking for.

```html
<!DOCTYPE html>
<html lang="en">
<head>
<meta charset="utf-8">
<title>Kalvendor Whitmane &amp; Associates – Business Card</title>
<link rel="stylesheet" href="https://fonts.googleapis.com/css2?family=Libre+Baskerville:wght@400;700&family=Marcellus&display=swap">
<style>
  :root {
    --stage: #2b2d31;
    --navy: #1f3a80;
    --paper: #ffffff;
    --slate: #7d7f84;
    --ink-light: #e8eef8;
  }
  * { margin: 0; padding: 0; box-sizing: border-box; }
  html, body {
    width: 1200px; height: 900px; overflow: hidden;
    background: var(--stage);
  }
  .stage { position: relative; width: 1200px; height: 900px; }
  .card {
    position: absolute; left: 285px;
    width: 630px; height: 360px;
    border-radius: 26px; overflow: hidden;
  }
  .card--front { top: 70px; background: var(--paper); }
  .card--back { top: 470px; background: var(--navy); }
  .card__shapes { position: absolute; inset: 0; }

  .holder-name {
    position: absolute; left: 34px; top: 36px;
    font-family: "Libre Baskerville", serif; font-weight: 700;
    font-size: 27px; color: var(--navy);
  }
  .contact-list {
    position: absolute; left: 30px; top: 118px;
    list-style: none;
    font-family: "Libre Baskerville", serif; font-size: 14px;
    color: var(--ink-light);
  }
  .contact-list li { display: flex; align-items: center; gap: 12px; height: 30px; }
  .contact-icon { width: 20px; height: 20px; flex: none; }

  .firm-mark { position: absolute; display: flex; align-items: center; }
  .firm-mark__square { flex: none; }
  .firm-mark__name {
    font-family: "Marcellus", serif; text-transform: uppercase;
    line-height: 1.05; letter-spacing: 0.04em;
  }
  .card--front .firm-mark { left: 360px; top: 112px; gap: 16px; }
  .card--front .firm-mark__square { width: 74px; height: 74px; background: var(--navy); }
  .card--front .firm-mark__name { font-size: 19px; color: var(--navy); }

  .card--back .firm-mark { left: 110px; top: 120px; gap: 26px; }
  .card--back .firm-mark__square { width: 120px; height: 120px; border: 1.5px solid rgba(255,255,255,0.55); }
  .card--back .firm-mark__name { font-size: 28px; color: var(--paper); }

  .address {
    position: absolute; left: 380px; top: 262px;
    display: flex; gap: 12px;
    font-family: "Libre Baskerville", serif; font-size: 14px; line-height: 1.5;
    color: var(--ink-light); font-style: normal;
  }
</style>
</head>
<body>
<main class="stage">

  <section class="card card--front">
    <svg class="card__shapes" viewBox="0 0 630 360" aria-hidden="true">
      <polygon points="0,95 250,95 360,240 630,240 630,360 0,360" fill="var(--navy)"/>
      <polygon points="250,95 290,95 300,125" fill="var(--slate)"/>
      <polygon points="0,322 220,322 180,360 0,360" fill="var(--slate)"/>
    </svg>

    <h1 class="holder-name">Martin Kalvendor, Esq.</h1>

    <ul class="contact-list">
      <li>
        <svg class="contact-icon" viewBox="0 0 20 20"><circle cx="10" cy="10" r="10" fill="var(--slate)"/><rect x="5" y="7" width="10" height="7" rx="1.5" fill="#fff"/><rect x="7" y="5" width="6" height="2.5" rx="1" fill="#fff"/></svg>
        <span>555.216.4093</span>
      </li>
      <li>
        <svg class="contact-icon" viewBox="0 0 20 20"><circle cx="10" cy="10" r="10" fill="var(--slate)"/><path d="M7 5.5 L9 8 L8 9.5 Q9 11.5 10.5 12 L12 11 L14.5 13 L13 14.5 Q8 14 5.5 7 Z" fill="#fff"/></svg>
        <span>555.370.8154</span>
      </li>
      <li>
        <svg class="contact-icon" viewBox="0 0 20 20"><circle cx="10" cy="10" r="10" fill="var(--slate)"/><rect x="5" y="6.5" width="10" height="7" fill="#fff"/><path d="M5 6.5 L10 10.5 L15 6.5" stroke="var(--slate)" stroke-width="1" fill="none"/></svg>
        <span>marty@kwlawfirm.example</span>
      </li>
      <li>
        <svg class="contact-icon" viewBox="0 0 20 20"><circle cx="10" cy="10" r="10" fill="var(--slate)"/><circle cx="10" cy="10" r="5" stroke="#fff" stroke-width="1.2" fill="none"/><path d="M5 10 H15 M10 5 V15" stroke="#fff" stroke-width="1"/></svg>
        <span>kalvendorwhitmanelaw.example</span>
      </li>
    </ul>

    <div class="firm-mark">
      <span class="firm-mark__square"></span>
      <p class="firm-mark__name">Kalvendor<br>Whitmane<br>&amp; Associates</p>
    </div>

    <address class="address">
      <svg class="contact-icon" viewBox="0 0 20 20"><circle cx="10" cy="10" r="10" fill="var(--slate)"/><path d="M10 15 L6.5 9.5 A4 4 0 1 1 13.5 9.5 Z" fill="#fff"/><circle cx="10" cy="8" r="1.5" fill="var(--slate)"/></svg>
      <span>48 Fennimore Lane,<br>2nd Floor Ashmere,<br>ME 04173</span>
    </address>
  </section>

  <section class="card card--back">
    <div class="firm-mark">
      <span class="firm-mark__square"></span>
      <p class="firm-mark__name">Kalvendor<br>Whitmane<br>&amp; Associates</p>
    </div>
  </section>

</main>
</body>
</html>
```